Referral card and Flyer design

Please see attached example of Flyer and Referral Card. I would like a similar type flyer and card but nicer design. Industrial/retro Automtive type design.

Referral card should be size of regular business card.

Flyer should be 8X10" typical printer paper size.

Business Logo and Name should be changed from Vantorel to GearHollow LLC and on flyer please remove the last option where it says ( a Night out on us ) .

Change address on referral card to
GearHollow LLC
412 N Pellam Rd
Youngsville NC 27583
GearHollowHaul.example
Call or Text 919-555-0147

```html
<!DOCTYPE html>
<html lang="en">
<head>
<meta charset="utf-8">
<title>GearHollow LLC – Pick Your Thank You Referral Flyer</title>
<link href="https://fonts.googleapis.com/css2?family=Archivo+Black&family=Roboto+Condensed:wght@300;700&display=swap" rel="stylesheet">
<style>
  :root {
    --frame-blue: #5a87a0;
    --panel-blue: #33607a;
    --cream: #f0e6da;
    --cream-shade: #d9c8b6;
    --sand-light: #f4ebe1;
    --sand-dark: #cbb6a1;
    --charcoal: #464646;
    --slate: #4f605f;
  }
  * { margin: 0; padding: 0; box-sizing: border-box; }
  html, body { width: 960px; height: 1200px; overflow: hidden; background: var(--frame-blue); }
  .flyer { position: relative; width: 960px; height: 1200px; overflow: hidden; }
  .backdrop { position: absolute; inset: 0; }
  .headline {
    position: absolute; left: 0; width: 960px; text-align: center;
    font-family: "Archivo Black", "Arial Black", sans-serif;
    color: var(--cream); line-height: 1;
  }
  .headline--main { top: 74px; font-size: 80px; line-height: 82px; }
  .headline--sub { top: 242px; font-size: 48px; }
  .step { position: absolute; left: 113px; display: flex; align-items: center; }
  .step__num {
    width: 61px; font-family: "Archivo Black", "Arial Black", sans-serif;
    font-size: 74px; color: var(--cream); line-height: 1;
  }
  .step__text {
    font-family: "Roboto Condensed", "Arial Narrow", sans-serif; font-weight: 300;
    font-size: 29px; color: var(--cream); white-space: nowrap;
  }
  .step__text strong { font-weight: 700; }
  .step--one { top: 306px; }
  .step--two { top: 384px; }
  .step--three { top: 580px; }
  .offer {
    position: absolute; left: 0; top: 458px; width: 980px; text-align: center;
    font-family: "Archivo Black", "Arial Black", sans-serif;
    font-size: 29px; line-height: 41.5px; letter-spacing: 2.4px; color: var(--cream);
  }
  .reward {
    position: absolute; text-align: center;
    font-family: "Archivo Black", "Arial Black", sans-serif; color: var(--cream);
  }
  .reward__amount { font-size: 64px; line-height: 1; color: var(--cream); text-shadow: 0 0 0 var(--cream-shade); }
  .reward__label { font-size: 28px; line-height: 30px; letter-spacing: 1px; }
  .reward--repairs { left: 290px; top: 702px; width: 220px; }
  .reward--repairs .reward__label { margin-top: 6px; }
  .reward--fuel { left: 656px; top: 652px; width: 220px; }
  .reward--fuel .reward__label { margin-top: 4px; }
  .art { position: absolute; border-radius: 6px; }
  .art--tools { left: 114px; top: 698px; width: 165px; height: 184px;
    background: radial-gradient(circle at 50% 40%, var(--cream), var(--cream-shade) 70%, transparent 72%); opacity: .85; }
  .art--pump { left: 706px; top: 762px; width: 143px; height: 320px; background: linear-gradient(90deg, #3e3e3e, #2f2f2f); }
  .brand {
    position: absolute; left: 0; top: 1018px; width: 960px; text-align: center;
    font-family: "Archivo Black", "Arial Black", sans-serif; font-size: 40px; color: var(--charcoal);
  }
  .cta {
    position: absolute; left: 0; top: 1110px; width: 935px; text-align: center;
    font-family: "Archivo Black", "Arial Black", sans-serif; font-size: 55px; color: var(--slate);
  }
</style>
</head>
<body>
<main class="flyer">
  <svg class="backdrop" width="960" height="1200" viewBox="0 0 960 1200" aria-hidden="true">
    <defs>
      <linearGradient id="sand" x1="0" y1="0" x2="1" y2="0">
        <stop offset="0" stop-color="var(--sand-dark)"/>
        <stop offset="0.45" stop-color="var(--sand-light)"/>
        <stop offset="1" stop-color="var(--sand-dark)"/>
      </linearGradient>
    </defs>
    <rect width="960" height="1200" fill="var(--frame-blue)"/>
    <rect x="22" y="22" width="916" height="1160" rx="4" fill="var(--panel-blue)"/>
    <polygon points="0,1023 960,740 960,1200 0,1200" fill="url(#sand)"/>
  </svg>

  <h1 class="headline headline--main">PICK YOUR<br>THANK YOU!</h1>
  <p class="headline headline--sub">Easy as 1 .. 2 .. 3!</p>

  <div class="step step--one"><span class="step__num">1</span><span class="step__text">We give you two <strong>REFERRAL CARDS</strong> with your name on them</span></div>
  <div class="step step--two"><span class="step__num">2</span><span class="step__text">Give the cards to a family member, friend or co-worker</span></div>

  <p class="offer">They present the card &amp; save<br>$25.00 on any service<br>No Strings Attached!</p>

  <div class="step step--three"><span class="step__num">3</span><span class="step__text">When a card is redeemed, as a thank you, you can choose either:</span></div>

  <div class="art art--tools" role="img" aria-label="Gear with crossed wrenches icon"></div>
  <div class="reward reward--repairs">
    <div class="reward__amount">$25.00</div>
    <div class="reward__label">CREDIT FOR<br>REPAIRS</div>
  </div>

  <div class="reward reward--fuel">
    <div class="reward__amount">$25.00</div>
    <div class="reward__label">FUEL CARD</div>
  </div>
  <div class="art art--pump" role="img" aria-label="Vintage gas pump illustration"></div>

  <p class="brand">GearHollow LLC</p>

  <p class="cta">Ask for YOUR cards today!</p>
</main>
</body>
</html>
```